Cleaning and Maintenance Business card design

i provide a service which includes;
Professional Window Cleaning
Lawn Mowing
Gardening
Painting
Rubbish Removal
Commercial Cleaning
Property & Ground Maintenance
Pensioner discounts apply
Call now for an inquiry and free quote
`Double sided` (willing to pay any extra)
i would like a design that is not too crowded and straight to the point.
i want the reader to know exactly what the business is about from one glance.
i would like the logo to communicate the businesses 3 main aspects (window cleaning, lawn mowing, and Cleaning)
Thanks.
Contact Information for Business Card
Business name : Brick 4 Leaf*
* with subline 'And Everything In Between' (smaller font)
Name: Tom Varkonisky
Mobile: 0417 582 903
Email: t.varkonisky@mailbrook.net
ABN: 47 915 230 861
`Double Sided`
Logo Text
Brick 4 Leaf

```html
<!DOCTYPE html>
<html lang="en">
<head>
<meta charset="utf-8">
<title>Brick 4 Leaf – Business Card</title>
<link rel="stylesheet" href="https://fonts.googleapis.com/css2?family=Open+Sans:ital,wght@0,400;0,700;1,400&display=swap">
<style>
  :root {
    --backdrop-light: #ececec;
    --backdrop-dark: #b4b4b4;
    --card: #ffffff;
    --brand-blue: #0b72b9;
    --brand-green: #109546;
    --ink: #1c1c1c;
  }
  html, body {
    margin: 0;
    padding: 0;
    overflow: hidden;
  }
  .canvas {
    position: relative;
    width: 986px;
    height: 1200px;
    overflow: hidden;
    background: radial-gradient(ellipse at 50% 50%, var(--backdrop-light) 0%, var(--backdrop-dark) 100%);
    font-family: "Open Sans", sans-serif;
    color: var(--ink);
  }
  .card {
    position: absolute;
    width: 816px;
    height: 477px;
    background: var(--card);
  }
  .card--front { left: 88px; top: 66px; }
  .card--back  { left: 91px; top: 640px; height: 474px; }
  .band {
    position: absolute;
    left: 0;
    width: 100%;
    height: 39px;
  }
  .band--top { top: 0; background: var(--brand-blue); }
  .band--bottom { bottom: 0; background: var(--brand-green); }

  .brand-square {
    position: absolute;
    left: 80px;
    top: 160px;
    width: 156px;
    height: 156px;
    border-radius: 10px;
    background: var(--brand-green);
  }
  .brand-name {
    position: absolute;
    left: 270px;
    top: 178px;
    margin: 0;
    font-size: 62px;
    font-weight: 400;
    line-height: 1;
    color: var(--ink);
    white-space: nowrap;
  }
  .brand-tagline {
    position: absolute;
    left: 311px;
    top: 268px;
    margin: 0;
    font-size: 28px;
    font-style: italic;
    line-height: 1;
    white-space: nowrap;
  }

  .back-name {
    position: absolute;
    left: 74px;
    top: 190px;
    margin: 0;
    font-size: 30px;
    font-weight: 400;
    line-height: 1;
    color: var(--ink);
    white-space: nowrap;
  }
  .contact {
    position: absolute;
    left: 284px;
    top: 164px;
    margin: 0;
    font-size: 26.5px;
    line-height: 34.5px;
  }
  .contact__person { font-weight: 700; }
  .services {
    position: absolute;
    left: 0;
    width: 100%;
    top: 394px;
    margin: 0;
    text-align: center;
    font-size: 24px;
    font-style: italic;
    line-height: 1;
  }
</style>
</head>
<body>
<main class="canvas">
  <section class="card card--front" aria-label="Card front">
    <div class="band band--top"></div>
    <div class="brand-square"></div>
    <h1 class="brand-name">Brick 4 Leaf</h1>
    <p class="brand-tagline">And Everything in Between</p>
    <div class="band band--bottom"></div>
  </section>

  <section class="card card--back" aria-label="Card back">
    <div class="band band--top"></div>
    <p class="back-name">Brick 4 Leaf</p>
    <address class="contact" style="font-style: normal;">
      <span class="contact__person">Tom Varkonisky</span><br>
      Mobile: 0417 582 903<br>
      Email: t.varkonisky@mailbrook.net<br>
      ABN: 47 915 230 861
    </address>
    <p class="services">Window cleaning, lawn care, and everything in between.</p>
    <div class="band band--bottom"></div>
  </section>
</main>
</body>
</html>
```